Business Card Design

We need two business cards - same design but with two different people's details.

We are a new start-up online cleaning business that allows people to book and pay for a quality home cleaner online.

We would like a professional yet overly formal style of business card.

Target Market(s)

18 - 65+ professionals

Industry/Entity Type

Business

Contact Information for Business Card

We would like two business cards but with the same design, the details are below:

Peter Valdoro
Director and Co-Founder
ph: 0421 573 916
Suite 3C, Level 4
517 Harwood Road
Belmira NSW 2089
peter@tidlo.com.au

_______________________________________________________

Evangelia Valdoro
Director and Co-Founder
ph: 0432 915047
Suite 3C, Level 4
517 Harwood Road
Belmira NSW 2089
evangelia@tidlo.com.au

Requirements
Must have
• although our style guide refers to orange and red, please stick to the blue/black/grey that is in the style guide.

also on the back of the card we would like the logo with our tag line which is on page 12 of the style guide.
Should not have
• no pictures of mops, cleaners etc

```html
<!DOCTYPE html>
<html lang="en">
<head>
<meta charset="utf-8">
<title>Tidlo Business Cards</title>
<link rel="stylesheet" href="https://fonts.googleapis.com/css2?family=Lexend:wght@600&family=Lexend+Exa:wght@500&family=Questrial&display=swap">
<style>
  :root {
    --backdrop: #e9e7e4;
    --card: #f7f7f6;
    --brand-blue: #12a5df;
    --ink: #1b1b1b;
    --ink-soft: #3a3a3a;
    --rule: #6d6d6d;
    --tagline: #555555;
  }
  * { margin: 0; padding: 0; box-sizing: border-box; }
  html, body {
    width: 1200px;
    height: 918px;
    overflow: hidden;
    background: var(--backdrop);
  }
  .stage { position: relative; width: 1200px; height: 918px; }
  .card {
    position: absolute;
    width: 580px;
    height: 358px;
    background: var(--card);
    box-shadow: 0 6px 16px rgba(0,0,0,0.22);
    font-family: "Questrial", sans-serif;
    color: var(--ink);
  }
  .card--peter { left: 38px; top: 50px; }
  .card--evangelia { left: 517px; top: 491px; }

  .brand { position: absolute; left: 394px; top: 28px; width: 180px; height: 60px; }
  .brand__name {
    display: block;
    font-family: "Lexend", sans-serif; font-weight: 600;
    font-size: 31px; line-height: 1; color: var(--ink-soft);
  }
  .brand__tagline {
    display: block; margin-top: 6px;
    font-size: 9.5px; color: var(--tagline); white-space: nowrap;
  }

  .accent-block {
    position: absolute; left: 0; top: 117px;
    width: 158px; height: 130px;
    background: var(--brand-blue);
  }

  .details { position: absolute; left: 170px; top: 117px; width: 393px; }
  .details__row {
    display: flex; align-items: center;
    border-bottom: 1px solid var(--rule);
    padding-left: 4px;
    white-space: nowrap;
  }
  .details__name {
    height: 28px;
    font-family: "Lexend Exa", sans-serif; font-weight: 500;
    font-size: 19px; letter-spacing: 0.2px;
  }
  .details__role { height: 40px; font-size: 15.5px; color: var(--ink-soft); padding-left: 6px; }
  .details__role .title { width: 130px; }
  .details__address { height: 35px; font-size: 14.6px; padding-left: 0; }
  .details__contact { border-bottom: none; height: 37px; font-size: 18.5px; letter-spacing: 0.3px; padding-left: 2px; }
  .sep { margin: 0 8px 0 4px; }
</style>
</head>
<body>
<main class="stage">

  <article class="card card--peter">
    <div class="brand">
      <span class="brand__name">Tidlo</span>
      <span class="brand__tagline">Trusted home cleaners booked in minutes</span>
    </div>
    <div class="accent-block"></div>
    <div class="details">
      <div class="details__row details__name">Peter&nbsp; Valdoro</div>
      <div class="details__row details__role"><span class="title">Director</span><span>|&nbsp; Co Founder</span></div>
      <div class="details__row details__address">Suite 3C, Level 4 517 Harwood Road Belmira NSW 2089</div>
      <div class="details__row details__contact"><span>0421 573 916</span><span class="sep">|</span><span>peter@tidlo.com.au</span></div>
    </div>
  </article>

  <article class="card card--evangelia">
    <div class="brand">
      <span class="brand__name">Tidlo</span>
      <span class="brand__tagline">Trusted home cleaners booked in minutes</span>
    </div>
    <div class="accent-block"></div>
    <div class="details">
      <div class="details__row details__name">Evangelia&nbsp; Valdoro</div>
      <div class="details__row details__role"><span class="title">Director</span><span>|&nbsp; Co Founder</span></div>
      <div class="details__row details__address">Suite 3C, Level 4 517 Harwood Road Belmira NSW 2089</div>
      <div class="details__row details__contact"><span>0432 915047</span><span class="sep">|</span><span>evangelia@tidlo.com.au</span></div>
    </div>
  </article>

</main>
</body>
</html>
```